Historic Church website

We want our church website to feel warm, historic, and clean, modern, and easy to navigate. Dont use the anchor

Current website: https://www.meadowlarkchapelhall.com/

Requirements
Should not have
• I would like to use the logo without the anchor

```html
<!DOCTYPE html>
<html lang="en">
<head>
<meta charset="utf-8">
<title>Meadowlark Chapel Hall</title>
<link rel="stylesheet" href="https://fonts.googleapis.com/css2?family=Bebas+Neue&family=Montserrat:wght@400;500;600;700&family=Roboto:wght@400;500&display=swap">
<style>
:root{
  --ink:#1d1613;
  --ink-2:#231a16;
  --ink-3:#2b211c;
  --gold:#c69a45;
  --gold-soft:#d7ae5c;
  --cream:#f3ece2;
  --white:#ffffff;
  --muted:#d9d2c8;
  --blue:#1f6fb0;
}
*{box-sizing:border-box;margin:0;padding:0}
html,body{width:1200px;height:4505px;overflow:hidden;background:var(--ink)}
body{position:relative;font-family:"Roboto",Arial,sans-serif;color:var(--white)}
.abs{position:absolute}
.btn{position:absolute;background:var(--gold);color:var(--white);font-family:"Montserrat",sans-serif;font-weight:700;font-size:14px;letter-spacing:.5px;border-radius:22px;display:flex;align-items:center;justify-content:center;text-transform:uppercase}
.section-title{position:absolute;display:flex;align-items:center;gap:14px;font-family:"Bebas Neue",sans-serif;font-size:44px;letter-spacing:.5px;color:var(--white)}
.title-mark{width:46px;height:46px;border:3px solid var(--white);border-radius:50%;flex:none}

/* header + hero */
.hero{left:0;top:0;width:1200px;height:820px;background:radial-gradient(ellipse at 50% 45%,#6b4a2c 0%,#3e2a1b 45%,#1e140e 100%)}
.hero-curve{left:0;top:600px;width:1200px;height:220px}
.nav{left:0;top:0;width:1200px;height:74px;background:rgba(29,22,19,.92)}
.nav a{position:absolute;top:34px;font-family:"Montserrat",sans-serif;font-size:13px;color:var(--white);text-decoration:none;white-space:nowrap}
.nav a.current{color:var(--gold)}
.nav a.current::after{content:"";position:absolute;left:0;right:0;top:24px;height:3px;background:var(--gold)}
.crest{left:515px;top:-60px;width:170px;height:170px;border-radius:50%;background:var(--ink);display:flex;flex-direction:column;align-items:center;justify-content:flex-end;padding-bottom:12px;z-index:2}
.crest-dot{width:28px;height:28px;border-radius:50%;border:3px solid var(--white);margin-bottom:6px}
.crest-name{font-family:"Montserrat",sans-serif;font-weight:700;font-size:30px;letter-spacing:3px;line-height:1}
.crest-est{font-family:"Montserrat",sans-serif;font-size:8px;letter-spacing:3px;color:var(--muted);margin-top:6px}
.hero-title{left:0;top:318px;width:1200px;text-align:center;font-family:"Bebas Neue",sans-serif;font-size:86px;line-height:86px;letter-spacing:1px;text-shadow:0 4px 14px rgba(0,0,0,.6)}

/* about */
.about-lead{left:114px;top:886px;width:460px;color:var(--gold);font-size:16px;line-height:25px}
.about-body{left:114px;top:955px;width:430px;font-size:13.5px;line-height:27px;color:var(--cream)}
.about-photo{left:654px;top:812px;width:414px;height:414px;border-radius:50%;background:linear-gradient(160deg,#8fa6c4 0%,#c9b9a6 40%,#8b7a66 75%,#3b2f27 100%)}

/* events */
.events{left:0;top:1322px;width:1200px;height:646px;background:var(--ink-2)}
.card{position:absolute;top:1469px;width:312px;height:356px;border-radius:6px;overflow:hidden}
.card-date{position:absolute;right:6px;top:6px;width:76px;height:68px;background:var(--gold);border-radius:6px;font-family:"Roboto",sans-serif;font-weight:500;font-size:17px;line-height:22px;display:flex;align-items:center;justify-content:center;text-align:center}
.card-title{position:absolute;left:14px;bottom:10px;font-family:"Roboto",sans-serif;font-weight:500;font-size:24px;text-shadow:0 2px 8px rgba(0,0,0,.8)}

/* verse banner */
.verse{left:0;top:1968px;width:1200px;height:556px;background:linear-gradient(90deg,#1b1410 0%,#2d2520 45%,#3b3430 100%)}
.verse-books{left:0;top:1990px;width:430px;height:534px;background:linear-gradient(90deg,#5a4a33 0%,#2d4a66 45%,#3f5e44 62%,#7a5a2e 80%,#4d2c1c 100%);opacity:.9}
.verse-text{left:492px;top:2078px;width:620px;font-family:"Montserrat",sans-serif;font-weight:700;font-size:42px;line-height:62px;letter-spacing:.5px}
.verse-ref{left:492px;top:2273px;font-family:"Montserrat",sans-serif;font-weight:700;font-size:34px}

/* visit */
.visit-item{position:absolute;top:2700px;width:300px;text-align:center}
.visit-ring{width:156px;height:156px;margin:0 auto;display:block}
.visit-time{font-size:16px;margin-top:4px}
.visit-name{font-size:21px;margin-top:22px}
.visit-note{font-size:15px;line-height:30px;margin-top:16px;color:var(--cream)}

/* testimonials */
.testi{left:0;top:3110px;width:1200px;height:452px;background:radial-gradient(ellipse at 50% 40%,#3a2d22 0%,#241a14 60%,#17110d 100%)}
.quote-mark{left:578px;top:3253px;width:46px;height:46px;border-radius:50%;background:#3e3127;font-family:"Montserrat",sans-serif;font-weight:700;font-size:34px;line-height:56px;text-align:center}
.testi-text{left:180px;top:3313px;width:840px;text-align:center;font-size:16px;line-height:33px}
.testi-name{left:0;top:3480px;width:1200px;text-align:center;font-weight:500;font-size:16px}
.arrow{width:22px;height:22px;border-radius:50%;display:flex;align-items:center;justify-content:center}

/* newsletter */
.news{left:0;top:3562px;width:1200px;height:640px;background:linear-gradient(90deg,#2a2421 0%,#342d29 55%,#4a3f37 100%)}
.news-art{left:760px;top:3570px;width:440px;height:470px;background:radial-gradient(ellipse at 55% 45%,#8a7560 0%,#4a3c32 50%,transparent 75%)}
.field{position:absolute;height:58px;border-radius:29px;background:var(--white);color:#333;font-size:14px;display:flex;align-items:center;padding-left:26px}

/* footer */
.footer{left:0;top:4190px;width:1200px;height:315px;background:var(--ink-2)}
.footer-dome{left:0;top:4040px;width:1200px;height:160px}
.brand-name{left:104px;top:4230px;width:330px;text-align:center;font-family:"Montserrat",sans-serif;font-weight:500;font-size:34px;letter-spacing:3px;line-height:44px}
.brand-est{left:104px;top:4368px;width:330px;text-align:center;font-family:"Montserrat",sans-serif;font-size:12px;letter-spacing:4px;color:var(--muted)}
.social{position:absolute;top:4414px;width:28px;height:28px;border-radius:50%;background:var(--white)}
.foot-head{position:absolute;top:4218px;font-family:"Montserrat",sans-serif;font-weight:700;font-size:16px}
.foot-links{left:556px;top:4252px;font-family:"Montserrat",sans-serif;font-size:13px;line-height:26px;list-style:none}
.contact-row{position:absolute;left:824px;display:flex;gap:18px;font-family:"Montserrat",sans-serif;font-size:13px;line-height:22px}
.contact-row svg{flex:none;margin-top:2px}
.copyright{left:0;top:4472px;width:1200px;text-align:center;font-family:"Montserrat",sans-serif;font-size:13px}
.copy-rule{left:108px;top:4460px;width:984px;height:1px;background:#5a4c42}
</style>
</head>
<body>

<!-- Hero -->
<div class="abs hero" role="img" aria-label="Warm library interior with leather armchairs, bookshelves and lamps"></div>
<svg class="abs hero-curve" viewBox="0 0 1200 220" preserveAspectRatio="none">
  <path d="M0 40 Q300 0 560 180 L600 215 L640 180 Q900 0 1200 40 L1200 220 L0 220 Z" fill="var(--ink)"/>
  <path d="M0 40 Q300 0 560 180 L600 215 L640 180 Q900 0 1200 40" fill="none" stroke="#3a2510" stroke-width="14"/>
</svg>

<nav class="abs nav">
  <a class="current" style="left:114px">Home</a>
  <a style="left:198px">About&nbsp; MCH</a>
  <a style="left:316px">Ministries</a>
  <a style="left:422px">Bible Studies</a>
  <a style="left:700px;top:28px">Sermon&nbsp; Library</a>
  <a style="left:848px;top:28px">Contact Us</a>
</nav>
<div class="btn" style="left:968px;top:18px;width:124px;height:42px;font-size:15px">Donate</div>

<div class="abs crest">
  <div class="crest-dot"></div>
  <div class="crest-name">MCH</div>
  <div class="crest-est">EST. 1928</div>
</div>

<h1 class="abs hero-title">Ancient Church. Ancient<br>Faith. Eternal Truth.</h1>
<div class="btn" style="left:487px;top:512px;width:226px;height:40px">Join Our Community</div>

<!-- About -->
<div class="section-title" style="left:112px;top:812px"><span class="title-mark"></span>About Us</div>
<p class="abs about-lead">Meadowlark Chapel Hall is an independent Christian church in the Protestant tradition.</p>
<p class="abs about-body">Its central tenets are found in its Articles of Faith and include belief in: the Deity and Lordship of Jesus Christ; the Trinity; Jesus' perfect life, atoning death on the cross, bodily resurrection, and ascension; Jesus' literal return; the inerrancy of the Bible in its original manuscripts; and our need for salvation through personal faith in Jesus Christ. In keeping with the prevailing perspective of the church during the centuries immediately following the Apostles, we teach Premillennialism.</p>
<div class="btn" style="left:112px;top:1186px;width:132px;height:42px">Read More</div>
<div class="abs about-photo" role="img" aria-label="Exterior of the church building with a palm tree and tower"></div>

<!-- Events -->
<div class="abs events"></div>
<div class="section-title" style="left:448px;top:1384px"><span class="title-mark"></span>Upcoming&nbsp; Events</div>

<div class="card" style="left:112px;background:linear-gradient(180deg,#5c4a36,#2a2018)" role="img" aria-label="Lantern glowing on a wooden table">
  <div class="card-date">Jan 18,<br>2026</div><div class="card-title">Sunday Service</div>
</div>
<div class="card" style="left:443px;background:linear-gradient(180deg,#6b5c4c,#3a2f26)" role="img" aria-label="Old world map hanging above a desk">
  <div class="card-date">Jan 21<br>2026</div><div class="card-title">Wednesday Night Bible</div>
</div>
<div class="card" style="left:775px;background:linear-gradient(180deg,#5a4632,#2b1f16)" role="img" aria-label="Antique map with candle and compass">
  <div class="card-date">Jan 25,<br>2026</div><div class="card-title">Sunday Service</div>
</div>
<div class="btn" style="left:512px;top:1871px;width:176px;height:40px">View Calendar</div>

<!-- Verse -->
<div class="abs verse"></div>
<div class="abs verse-books" role="img" aria-label="Row of old leather-bound theology books"></div>
<p class="abs verse-text">WE HAVE THIS HOPE AS AN ANCHOR FOR THE SOUL, FIRM AND SECURE.</p>
<p class="abs verse-ref">- HEB 6:19</p>
<div class="btn" style="left:501px;top:2348px;width:260px;height:40px">Join This Week Sermon</div>

<!-- Visit -->
<div class="section-title" style="left:428px;top:2606px"><span class="title-mark"></span>Visit Us This Sunday</div>

<div class="visit-item" style="left:130px">
  <svg class="visit-ring" viewBox="0 0 156 156">
    <path d="M30 130 A68 68 0 1 1 126 130" fill="none" stroke="var(--white)" stroke-width="9"/>
    <circle cx="78" cy="78" r="52" fill="#3a241a"/>
    <rect x="58" y="60" width="28" height="20" fill="none" stroke="var(--white)" stroke-width="3"/>
    <circle cx="96" cy="62" r="5" fill="var(--white)"/>
    <rect x="92" y="70" width="9" height="22" fill="var(--white)"/>
    <circle cx="62" cy="92" r="4" fill="var(--white)"/><circle cx="76" cy="92" r="4" fill="var(--white)"/>
    <path d="M34 138 Q78 118 122 138" fill="none" stroke="var(--white)" stroke-width="6"/>
  </svg>
  <p class="visit-time">11.00 am</p>
  <p class="visit-name">Morning Workshop Service</p>
  <p class="visit-note">Sunday morning worship and<br>service takes place in the<br>main sanctuary.</p>
</div>
<div class="visit-item" style="left:455px">
  <svg class="visit-ring" viewBox="0 0 156 156">
    <path d="M30 130 A68 68 0 1 1 126 130" fill="none" stroke="var(--white)" stroke-width="9"/>
    <circle cx="78" cy="78" r="52" fill="var(--gold)"/>
    <path d="M52 86 A26 26 0 0 1 104 86 Z" fill="var(--white)"/>
    <rect x="46" y="88" width="64" height="5" rx="2" fill="var(--white)"/>
    <circle cx="78" cy="57" r="4" fill="var(--white)"/>
    <path d="M34 138 Q78 118 122 138" fill="none" stroke="var(--white)" stroke-width="6"/>
  </svg>
  <p class="visit-time">12.15 pm</p>
  <p class="visit-name">All Church Lunch</p>
  <p class="visit-note">• Family Room •<br>Please join us for lunch after<br>the service.Everyone is<br>welcome!</p>
</div>
<div class="visit-item" style="left:773px">
  <svg class="visit-ring" viewBox="0 0 156 156">
    <path d="M30 130 A68 68 0 1 1 126 130" fill="none" stroke="var(--white)" stroke-width="9"/>
    <circle cx="78" cy="78" r="52" fill="#3a241a"/>
    <path d="M54 58 Q66 54 75 60 L75 100 Q66 94 54 98 Z M81 60 Q90 54 102 58 L102 98 Q90 94 81 100 Z" fill="var(--white)"/>
    <path d="M34 138 Q78 118 122 138" fill="none" stroke="var(--white)" stroke-width="6"/>
  </svg>
  <p class="visit-time">12.45 pm</p>
  <p class="visit-name">Afternoon Adult Bible Study</p>
  <p class="visit-note">Patio Room<br>TBA</p>
</div>

<!-- Testimonials -->
<div class="abs testi" role="img" aria-label="Dim background of antique maps and instruments"></div>
<div class="section-title" style="left:428px;top:3178px"><span class="title-mark"></span>Client Testimonials</div>
<div class="abs quote-mark">“</div>
<p class="abs testi-text">"The great need across evangelicalism is exposition of the Scriptures. I sense there is a departure from that, even amongst some of our own grads who are entertaining the people, giving the people what they want, whereas we are called to teach the Word. It is the Word that is the power of God to salvation; it is the Word that is the power for Christian living, and (the Word should be) the center of their ministry. It may not be popular, it may not build mega-churches, but it will fulfill that to which they are called upon to do in ministry.</p>
<p class="abs testi-name">Harold Whitcombe</p>
<div class="abs arrow" style="left:39px;top:3387px;background:var(--gold)"><svg width="10" height="10" viewBox="0 0 10 10"><path d="M7 1 L3 5 L7 9" fill="none" stroke="#1d1613" stroke-width="2"/></svg></div>
<div class="abs arrow" style="left:1138px;top:3377px;background:var(--white)"><svg width="10" height="10" viewBox="0 0 10 10"><path d="M3 1 L7 5 L3 9" fill="none" stroke="#1d1613" stroke-width="2"/></svg></div>

<!-- Newsletter -->
<div class="abs news"></div>
<div class="abs news-art" role="img" aria-label="Wall clock hanging above a shelf with books and headphones"></div>
<div class="section-title" style="left:114px;top:3666px"><span class="title-mark"></span>Sign Up For Our Weekly Newsletter</div>
<div class="field" style="left:110px;top:3769px;width:282px">First Name</div>
<div class="field" style="left:411px;top:3769px;width:283px">Last Name</div>
<div class="field" style="left:110px;top:3844px;width:586px">Email Address</div>
<div class="btn" style="left:115px;top:3918px;width:106px;height:40px">Send</div>

<!-- Footer -->
<svg class="abs footer-dome" viewBox="0 0 1200 160" preserveAspectRatio="none">
  <path d="M0 150 L440 150 Q600 20 760 150 L1200 150 L1200 160 L0 160 Z" fill="var(--ink-2)"/>
</svg>
<div class="abs footer"></div>
<div class="abs" style="left:560px;top:4070px;width:80px;height:80px;border-radius:50%;border:4px solid var(--white)"></div>

<p class="abs brand-name">Meadowlark<br>Chapel Hall</p>
<p class="abs brand-est">— EST. 1928 —</p>
<span class="social" style="left:114px;background:var(--gold)"></span>
<span class="social" style="left:148px"></span>
<span class="social" style="left:182px"></span>
<span class="social" style="left:216px"></span>

<p class="foot-head" style="left:556px">QUICK LINKS</p>
<ul class="abs foot-links">
  <li>Home</li><li>About&nbsp; MCH</li><li>Ministries</li><li>Bible&nbsp; Studies</li><li>Sermon Library</li><li>Contact Us</li>
</ul>

<p class="foot-head" style="left:824px">CONTACT INFO</p>
<div class="contact-row" style="top:4256px">
  <svg width="22" height="24" viewBox="0 0 22 24"><path d="M11 1 A8 8 0 0 1 19 9 C19 15 11 23 11 23 C11 23 3 15 3 9 A8 8 0 0 1 11 1 Z" fill="var(--white)"/><circle cx="11" cy="9" r="3" fill="var(--ink-2)"/></svg>
  <span>4120 Linden Row<br>Fairhaven, Oregon 97310</span>
</div>
<div class="contact-row" style="top:4334px">
  <svg width="22" height="22" viewBox="0 0 22 22"><circle cx="11" cy="11" r="11" fill="var(--white)"/><path d="M7 6 L9 6 L10 9 L8.5 10 Q10 13 12 13.5 L13 12 L16 13 L16 15 Q15 16.5 13 16 Q7 14 6 8 Q6 6.5 7 6 Z" fill="var(--ink-2)"/></svg>
  <span>555.204.7713</span>
</div>
<div class="contact-row" style="top:4384px">
  <svg width="22" height="22" viewBox="0 0 22 22"><circle cx="11" cy="11" r="11" fill="var(--white)"/><rect x="5.5" y="7" width="11" height="8" fill="none" stroke="var(--ink-2)" stroke-width="1.6"/><path d="M5.5 7 L11 11.5 L16.5 7" fill="none" stroke="var(--ink-2)" stroke-width="1.6"/></svg>
  <span>info@meadowlarkchapelhall.com</span>
</div>

<div class="abs copy-rule"></div>
<p class="abs copyright">© Copyright 2026&nbsp; |&nbsp; Meadowlark Chapel Hall, Eastbrook, Fairhaven, Oregon&nbsp; All Rights Reserved</p>

</body>
</html>
```